Need Bus charter business website,

I am starting a bus charter business in the near future. I am based in Geelong, Victoria in Australia. I will have a 25 or 28 seater bus that will be used to take people on charted trips. Whether they be to birthday parties, weddings, sporting events, corporate events, mystery trips, going down the Great Ocean Road, or anywhere someone wants. As for colour scheme, I'm leaning towards something blue and grey, but open to anything really that catches my eye. I played around with a basic web design program and made a basic site which I uploaded ( www.kelmoride.com.au) It has things which I wanted to include such as, services I will provide, trip information, contact form etc.

I don't mind if the layout is completely different to my site as it was only a template that was included in the program I used. I would like the overall design to be relatively fluid, not having to back-track a lot to navigate the site.

```html
<!DOCTYPE html>
<html lang="en">
<head>
<meta charset="utf-8">
<title>Kelmo Ride Tours</title>
<link rel="stylesheet" href="https://fonts.googleapis.com/css2?family=Arimo:ital,wght@0,400;0,700;1,400&family=Marcellus&family=Open+Sans:wght@700&display=swap">
<style>
:root{
  --navy:#1f4e79;
  --blue:#2b5a85;
  --ink:#222;
  --heading:#555;
  --text:#888;
  --rule:#d9d9d9;
  --footer:#2e2e2e;
  --footer-text:#a8a8a8;
  --white:#fff;
}
*{margin:0;padding:0;box-sizing:border-box}
html,body{width:715px;height:1200px;overflow:hidden;background:var(--white)}
body{position:relative;font-family:Arimo,Arial,sans-serif;color:var(--text)}
.abs{position:absolute}
.site-header{left:0;top:0;width:715px;height:66px;border-top:2px solid var(--navy);background:var(--white)}
.brand{left:78px;top:20px;font-family:Marcellus,serif;font-size:15px;color:var(--ink);display:flex;align-items:center;gap:6px}
.brand-dot{width:8px;height:8px;border-radius:50%;background:var(--navy)}
.main-nav{top:31px;font-size:7.2px;text-transform:uppercase;color:#333;letter-spacing:.1px}
.main-nav.active{color:var(--navy)}
.hero{left:0;top:66px;width:715px;height:291px;background:linear-gradient(180deg,#4a88c9 0%,#8dbbe3 38%,#c9d6b0 60%,#b9a748 78%,#5b5a3e 100%)}
.hero-title{left:363px;top:80px;font-family:Marcellus,serif;font-size:37px;color:var(--white)}
.hero-copy{left:365px;top:125px;width:250px;font-size:6.6px;line-height:15px;color:#1a1a1a}
.hero-arrow{top:188px}
.section-title{font-family:"Open Sans",sans-serif;font-weight:700;font-size:16.5px;color:var(--heading);text-transform:uppercase}
.center{left:0;width:715px;text-align:center}
.lead{font-size:6.8px;line-height:12.5px;color:var(--text)}
.card-photo{top:438px;width:125px;height:95px;border:1px solid #ddd;padding:2px;background:var(--white)}
.card-photo div{width:100%;height:100%}
.card-title{top:546px;font-family:Marcellus,serif;font-size:12.5px;color:var(--ink)}
.card-text{top:569px;width:130px;font-size:6.8px;line-height:11.5px;font-style:italic;color:var(--text)}
.card-rule{top:613px;width:126px;height:1px;background:var(--rule)}
.read-more{font-size:6.6px;color:#333;text-transform:uppercase;display:flex;align-items:center;gap:3px}
.rule{height:1px;background:var(--rule)}
.news-date{left:78px;width:30px;text-align:center;font-family:"Open Sans",sans-serif;font-weight:700;color:var(--blue);font-size:16px;line-height:16px}
.news-date span{display:block;font-size:7px;line-height:9px}
.news-title{left:109px;font-size:7.6px;color:var(--blue);text-transform:uppercase}
.news-text{left:110px;width:175px;font-size:6.8px;line-height:11.5px;color:var(--text)}
.news-more{left:110px;font-size:6.8px;font-weight:700;color:#444;text-transform:uppercase}
.book-lead{left:322px;top:706px;width:310px;font-size:6.8px;line-height:12px;color:var(--blue);text-transform:uppercase}
.book-photo{left:322px;top:736px;width:314px;height:112px;border:1px solid #ddd;padding:2px}
.book-photo div{width:100%;height:100%;background:linear-gradient(90deg,#d9a21a,#e8c23a 40%,#7d9fc4 70%,#c9a36d)}
.book-text{left:322px;top:855px;width:314px;font-size:6.8px;line-height:11.5px;color:var(--text)}
.cta{left:302px;top:1037px;width:112px;height:31px;background:var(--blue);border-bottom:2px solid #1a3d5e;color:var(--white);font-size:11.5px;text-align:center;line-height:30px;text-transform:uppercase}
.site-footer{left:0;top:1079px;width:715px;height:121px;background:var(--footer)}
.social{top:1098px;width:30px;height:30px;border:1.5px solid #888;border-radius:50%}
.footer-nav{top:1144px;font-size:6.8px;color:var(--footer-text);word-spacing:1px}
.copyright{top:1168px;font-size:6.5px;color:var(--footer-text)}
</style>
</head>
<body>
<header class="site-header abs">
  <div class="brand abs"><span class="brand-dot"></span>Kelmo Ride Tours</div>
  <span class="main-nav active abs" style="left:259px">Kelmo Ride Tours</span>
  <span class="main-nav abs" style="left:335px">About Us</span>
  <span class="main-nav abs" style="left:392px">Services</span>
  <span class="main-nav abs" style="left:449px">Trips on Offers</span>
  <span class="main-nav abs" style="left:530px">Book a Trip</span>
  <span class="main-nav abs" style="left:596px">Contact Us</span>
</header>

<section class="hero abs" role="img" aria-label="Photo of a white coach on a country road beside golden grass under a blue sky"></section>
<h1 class="hero-title abs">Kelmo Ride Tours</h1>
<p class="hero-copy abs">We are an accredited bus company that operates bus trip and charter work in the Geelong area. We offer a range of services, from day trips down the Great Ocean Road, to transport for wedding guests, Buck's and Hen's nights or school trips.</p>
<svg class="hero-arrow abs" style="left:47px" width="18" height="40" viewBox="0 0 18 40"><polyline points="15,3 3,20 15,37" fill="none" stroke="rgba(90,90,90,.7)" stroke-width="3"/></svg>
<svg class="hero-arrow abs" style="left:656px" width="18" height="40" viewBox="0 0 18 40"><polyline points="3,3 15,20 3,37" fill="none" stroke="rgba(255,255,255,.6)" stroke-width="3"/></svg>

<h2 class="section-title abs center" style="top:367px">Welcome to Kelmo Ride Tours</h2>
<p class="lead abs center" style="top:398px;left:117px;width:481px">We are an accredited bus company that operates bus trip and charter work in the Geelong area. We offer a range of services, from day trips down the Great Ocean Road, to transport for wedding guests, Buck's and Hen's nights or school trips</p>

<div class="card-photo abs" style="left:78px"><div role="img" aria-label="Photo of a bride and groom beside a coach" style="background:linear-gradient(135deg,#8a9aa6,#e6e2dc 50%,#6f8a4a)"></div></div>
<div class="card-photo abs" style="left:222px"><div role="img" aria-label="Photo of a group of friends enjoying a winery tour bus" style="background:linear-gradient(135deg,#b08a5a,#d8c7a3 50%,#7a9a86)"></div></div>
<div class="card-photo abs" style="left:365px"><div role="img" aria-label="Photo of passengers riding a bus to an event" style="background:linear-gradient(135deg,#3a6ea5,#d9c27a 50%,#9aa8b8)"></div></div>
<div class="card-photo abs" style="left:509px"><div role="img" aria-label="Photo of young women chatting on a bus" style="background:linear-gradient(135deg,#9ab8d0,#e1d6cc 50%,#5a6e82)"></div></div>

<h3 class="card-title abs" style="left:79px">Weddings</h3>
<h3 class="card-title abs" style="left:220px">Winery Tours</h3>
<h3 class="card-title abs" style="left:365px">Corporate Events</h3>
<h3 class="card-title abs" style="left:509px">Hens Party</h3>

<p class="card-text abs" style="left:78px">Lorem ipsum dolor sit amet, cons loectet ur adipisicing elit, sed do eiusmodjllo tem por incididunt ut labore et .</p>
<p class="card-text abs" style="left:222px">Lorem ipsum dolor sit amet, cons loectet ur adipisicing elit, sed do eiusmodjllo tem por incididunt ut labore et .</p>
<p class="card-text abs" style="left:365px">Lorem ipsum dolor sit amet, cons loectet ur adipisicing elit, sed do eiusmodjllo tem por incididunt ut labore et .</p>
<p class="card-text abs" style="left:509px">Lorem ipsum dolor sit amet, cons loectet ur adipisicing elit, sed do eiusmodjllo tem por incididunt ut labore et .</p>

<div class="card-rule abs" style="left:78px"></div>
<div class="card-rule abs" style="left:222px"></div>
<div class="card-rule abs" style="left:365px"></div>
<div class="card-rule abs" style="left:509px"></div>

<a class="read-more abs" style="left:78px;top:625px"><svg width="8" height="8" viewBox="0 0 8 8"><circle cx="4" cy="4" r="4" fill="#1f3b57"/><polyline points="3,2 5,4 3,6" fill="none" stroke="#fff" stroke-width="1.2"/></svg>Read More</a>
<a class="read-more abs" style="left:222px;top:625px"><svg width="8" height="8" viewBox="0 0 8 8"><circle cx="4" cy="4" r="4" fill="#1f3b57"/><polyline points="3,2 5,4 3,6" fill="none" stroke="#fff" stroke-width="1.2"/></svg>Read More</a>
<a class="read-more abs" style="left:365px;top:625px"><svg width="8" height="8" viewBox="0 0 8 8"><circle cx="4" cy="4" r="4" fill="#1f3b57"/><polyline points="3,2 5,4 3,6" fill="none" stroke="#fff" stroke-width="1.2"/></svg>Read More</a>
<a class="read-more abs" style="left:509px;top:625px"><svg width="8" height="8" viewBox="0 0 8 8"><circle cx="4" cy="4" r="4" fill="#1f3b57"/><polyline points="3,2 5,4 3,6" fill="none" stroke="#fff" stroke-width="1.2"/></svg>Read More</a>

<div class="rule abs" style="left:78px;top:654px;width:559px"></div>

<h2 class="section-title abs" style="left:78px;top:668px">Latest News</h2>
<h2 class="section-title abs" style="left:318px;top:668px">Want to Book a Trip?</h2>
<div class="abs" style="left:298px;top:708px;width:1px;height:217px;background:var(--rule)"></div>

<div class="news-date abs" style="top:706px">13<span>JULY</span></div>
<h4 class="news-title abs" style="top:708px">Kelmo Ride Tours is a family run business</h4>
<p class="news-text abs" style="top:724px">Lorem ipsum dolor sit amet, conc tetur adipi scing. Praesent vestibuum motie lacuiirhs. Aenean non.</p>
<span class="news-more abs" style="top:752px">Read More</span>
<div class="rule abs" style="left:78px;top:772px;width:195px"></div>

<div class="news-date abs" style="top:787px">20<span>JULY</span></div>
<h4 class="news-title abs" style="top:789px">Kelmo Ride Tours is a family run business</h4>
<p class="news-text abs" style="top:806px">Lorem ipsum dolor sit amet, conc tetur adipi scing. Praesent vestibuum motie lacuiirhs. Aenean non.</p>
<span class="news-more abs" style="top:834px">Read More</span>
<div class="rule abs" style="left:78px;top:855px;width:195px"></div>

<div class="news-date abs" style="top:871px">12<span>JULY</span></div>
<h4 class="news-title abs" style="top:873px">Kelmo Ride Tours is a family run business</h4>
<p class="news-text abs" style="top:890px">Lorem ipsum dolor sit amet, conc tetur adipi scing. Praesent vestibuum motie lacuiirhs. Aenean non.</p>
<span class="news-more abs" style="top:918px">Read More</span>

<p class="book-lead abs">Kelmo Ride Tours is a family run business. We pride ourselves on providing great service and value for money explore more of it with you.</p>
<div class="book-photo abs"><div role="img" aria-label="Photo of happy children waving from the windows of a yellow school bus"></div></div>
<p class="book-text abs">Aenean non ummy dreriauris. Phasellllus. porta. Fusce suscipit variusium sociis totdnatibus et magis dis parturient montes, nasceidiculus mus. Nulla dui. Fusce feugiatle. suada odio. Morbi nunc odio, gravida at.Lorem ipsum dolor sit amet, conc tetur adipi scing. Praesent vesti-buum molstie lacuiirhs. Aenean non ummy dreriauris. Phasellllus.</p>
<span class="news-more abs" style="left:322px;top:916px">Read More</span>

<div class="rule abs" style="left:78px;top:939px;width:559px"></div>

<h2 class="section-title abs center" style="top:946px">About Us</h2>
<p class="lead abs center" style="top:977px;left:108px;width:499px;line-height:16.5px">Kelmo Ride Tours is a family run business. We pride ourselves on providing great service and value for money. We know and love the Geelong region and want to explore more of it with you.We are an accredited bus company that operates bus trip and charter work in the Geelong area. We offer a range of services, from day trips down the Great Ocean Road, to transport for wedding guests, Buck's and Hen's nights or school trips</p>
<a class="cta abs">Read More</a>

<footer class="site-footer abs"></footer>
<span class="social abs" style="left:262px"></span>
<span class="social abs" style="left:303px"></span>
<span class="social abs" style="left:343px"></span>
<span class="social abs" style="left:383px"></span>
<span class="social abs" style="left:422px"></span>
<nav class="footer-nav abs center">Kelmo Ride Tours &nbsp;&nbsp; | &nbsp;&nbsp; About Us &nbsp;&nbsp; | &nbsp;&nbsp; Services &nbsp;&nbsp; | &nbsp;&nbsp; Trips on Offers &nbsp;&nbsp; | &nbsp;&nbsp; Book a Trip &nbsp;&nbsp; | &nbsp;&nbsp; Contact Us</nav>
<p class="copyright abs center">© Copy Rights 2014 Kelmo Ride Tours. All Rights Reserved.</p>
</body>
</html>
```